landing pages for BidPanel split testing

professional services

tattoo studio

SPA

We need to improve conversions, load speed and lumo ads quality score to be priority

Content is ready copy and visual

Just need a few extra ideas to test

https://ridgewaypartners.com.au/

Current website

https://property.ridgewaypartners.com.au/

1 landing page for ads

We would like to test something a little visually pleasing while in the past simple even ugly has work we are missing the mark

https://byvelo.co/?utm_source=LumoSearchNetwork&utm_medium=cpc&utm_device=m&utm_campaign=30000028802&utm_adgroup=274801592443&utm_keyword=buyers%20agent&utm_matchtype=p&utm_placement=&utm_adposition=&utm_location=8284267&keyword_k=buyers%20agent&utm_term=buyers%20agent&gclid={var:gclid}&gad_source=1&gclid=DkxLDBkxrsf2CiBrFjxB8h0Rij-gPpTytbZaphPxBtgIB2dQV81tsyOyscSyR_Er_LyCirWuvUgyuSpDnvxRBwE_CxCF

Here are the biggest ad spends in the market to date

Target Market(s)

People who are looking to get into the property market either invest or.home who want the head ache of negotiation gone, or don't know where to look , building wealth through property

Industry/Entity Type

Investment property buyers Agent

Coding

Coded - Design and coding required

Font styles to use
Other font styles liked:
• Keep to current

Requirements
Must have
• Don't change our copy for the ads landing page just need to flow better placement etc with call to action, remove the long winded steps , as some.more examples of example.properties
Nice to have
• Call to actions placed as they are ( keep to the original websites colour scheme )
Should not have
• Remove and reference to financial planning

```html
<!DOCTYPE html>
<html lang="en">
<head>
<meta charset="UTF-8">
<title>Quillbrook Property — Smart Investments for Long-Term Growth</title>
<link rel="stylesheet" href="https://fonts.googleapis.com/css2?family=Montserrat:wght@400;500;600;700;800&display=swap">
<style>
  :root {
    --navy: #0d3350;
    --navy-deep: #07304d;
    --blue-mid: #1d5f8a;
    --ink: #111821;
    --text: #2b3a48;
    --green: #4fc41c;
    --pill-bg: #e4ebf0;
    --white: #ffffff;
  }
  * { margin: 0; padding: 0; box-sizing: border-box; }
  html, body { width: 1200px; height: 675px; overflow: hidden; background: var(--white); }
  body { font-family: "Montserrat", sans-serif; color: var(--text); }
  a { text-decoration: none; }

  .hero { position: relative; width: 1200px; height: 675px; overflow: hidden; background: var(--white); }

  .hero-backdrop {
    position: absolute; inset: 0;
    background:
      radial-gradient(ellipse 420px 320px at 560px 260px, rgba(196,206,214,.55), transparent 70%),
      radial-gradient(ellipse 300px 360px at 250px 240px, rgba(214,222,228,.5), transparent 70%),
      linear-gradient(100deg, #f4f6f8 0%, #eef2f5 45%, #f7f9fb 70%, #ffffff 100%);
  }

  .bottom-edge { position: absolute; inset: 0; width: 1200px; height: 675px; }

  .brand { position: absolute; left: 88px; top: 54px; display: flex; align-items: center; gap: 10px; }
  .brand-mark { width: 34px; height: 34px; background: var(--navy); border-radius: 50%; }
  .brand-name { font-weight: 700; font-size: 24px; letter-spacing: 2px; color: var(--navy); }

  .contact-pill {
    position: absolute; left: 868px; top: 42px; width: 243px; height: 59px;
    border: 2px solid var(--navy); border-radius: 30px; background: var(--pill-bg);
    display: flex; align-items: center; padding-left: 9px; gap: 10px;
  }
  .contact-icon { width: 39px; height: 39px; border-radius: 50%; background: var(--navy); display: flex; align-items: center; justify-content: center; flex: none; }
  .contact-text { display: flex; flex-direction: column; }
  .contact-label { font-size: 12.5px; font-weight: 600; color: var(--navy); letter-spacing: .3px; line-height: 1.15; }
  .contact-number { font-size: 19px; font-weight: 700; color: var(--ink); line-height: 1.2; }

  .headline { position: absolute; left: 167px; top: 155px; font-size: 32px; line-height: 38px; font-weight: 500; color: var(--ink); letter-spacing: .8px; }
  .headline strong { font-weight: 800; }

  .tagline { position: absolute; left: 168px; top: 254px; display: flex; align-items: center; gap: 8px; font-size: 13.5px; color: var(--navy); letter-spacing: .3px; }
  .tagline::before { content: ""; width: 79px; height: 1px; background: var(--navy); }

  .benefits { position: absolute; left: 168px; top: 292px; list-style: none; }
  .benefits li { display: flex; align-items: center; gap: 9px; font-size: 13px; height: 30.5px; color: var(--text); }

  .cta { position: absolute; left: 168px; width: 329px; height: 40px; border-radius: 20px; display: flex; align-items: center; color: var(--white); font-weight: 700; font-size: 11px; }
  .cta-call { top: 447px; background: linear-gradient(90deg, var(--navy-deep), var(--blue-mid)); padding-left: 11px; letter-spacing: .1px; }
  .cta-play { position: absolute; right: -13px; top: 7px; width: 27px; height: 27px; border-radius: 50%; background: var(--white); display: flex; align-items: center; justify-content: center; }
  .cta-chat { top: 495px; background: var(--green); justify-content: center; gap: 6px; }

  .advisor-photo {
    position: absolute; left: 668px; top: 88px; width: 342px; height: 540px;
    border-radius: 150px 150px 0 0;
    background: linear-gradient(180deg, #b88d68 0%, #c9a386 22%, #d4d6d8 48%, #c3c6ca 80%, #b5b9bd 100%);
  }
</style>
</head>
<body>
<main class="hero">
  <div class="hero-backdrop" role="img" aria-label="Softly blurred modern office building backdrop"></div>

  <div class="advisor-photo" role="img" aria-label="Portrait of a smiling property advisor in a light grey blazer"></div>

  <svg class="bottom-edge" viewBox="0 0 1200 675" preserveAspectRatio="none" aria-hidden="true">
    <path d="M0 560 Q600 680 1200 560 L1200 675 L0 675 Z" fill="#ffffff"/>
    <path d="M0 560 Q600 680 1200 560" fill="none" stroke="#0d3350" stroke-width="2"/>
  </svg>

  <div class="brand">
    <span class="brand-mark"></span>
    <span class="brand-name">QUILLBROOK PROPERTY</span>
  </div>

  <a class="contact-pill" href="tel:+61400555018">
    <span class="contact-icon">
      <svg width="22" height="22" viewBox="0 0 24 24" fill="none" stroke="#fff" stroke-width="1.8"><circle cx="12" cy="12" r="10"/><path d="M9 7c-1 1-1 3 1 6s4 4 5 3l1-1-2-2-1 1c-1-.5-2-1.5-2.5-2.5l1-1-2-2z" fill="#fff" stroke="none"/></svg>
    </span>
    <span class="contact-text">
      <span class="contact-label">CONTACT US</span>
      <span class="contact-number">+61 400 555 018</span>
    </span>
  </a>

  <h1 class="headline">SMART INVESTMENTS<br>FOR <strong>LONG-TERM GROWTH</strong></h1>

  <p class="tagline">THE RIGHT INVESTMENT ISN'T JUST ABOUT TODAY</p>

  <ul class="benefits">
    <li><svg width="14" height="14" viewBox="0 0 14 14"><rect x="1" y="2" width="11" height="11" fill="none" stroke="#0d3350" stroke-width="1.6"/><path d="M3.5 7.5l2.5 2.5L13 2" fill="none" stroke="#0d3350" stroke-width="2"/></svg>Buy an Investment you never have to sell</li>
    <li><svg width="14" height="14" viewBox="0 0 14 14"><rect x="1" y="2" width="11" height="11" fill="none" stroke="#0d3350" stroke-width="1.6"/><path d="M3.5 7.5l2.5 2.5L13 2" fill="none" stroke="#0d3350" stroke-width="2"/></svg>Sustain long term capital growth</li>
    <li><svg width="14" height="14" viewBox="0 0 14 14"><rect x="1" y="2" width="11" height="11" fill="none" stroke="#0d3350" stroke-width="1.6"/><path d="M3.5 7.5l2.5 2.5L13 2" fill="none" stroke="#0d3350" stroke-width="2"/></svg>Affordable Investments that can be held long term</li>
    <li><svg width="14" height="14" viewBox="0 0 14 14"><rect x="1" y="2" width="11" height="11" fill="none" stroke="#0d3350" stroke-width="1.6"/><path d="M3.5 7.5l2.5 2.5L13 2" fill="none" stroke="#0d3350" stroke-width="2"/></svg>Free affordability and growth assessments</li>
  </ul>

  <a class="cta cta-call" href="#schedule">SCHEDULE A CALL FOR CUSTOMIZED ASSSESMENT
    <span class="cta-play"><svg width="11" height="11" viewBox="0 0 12 12"><path d="M3 1.5l7 4.5-7 4.5z" fill="none" stroke="#111821" stroke-width="1.6" stroke-linejoin="round"/></svg></span>
  </a>

  <a class="cta cta-chat" href="#message">
    <svg width="14" height="14" viewBox="0 0 24 24" fill="none" stroke="#fff" stroke-width="2"><rect x="3" y="4" width="18" height="13" rx="3"/><path d="M8 17l-2 4 6-4"/></svg>
    MESSAGE US
  </a>
</main>
</body>
</html>
```